Car Design - New van

It's Marisol and Tom from Larkin the Plumber.

Below is the vehicle - it is a Rovanta Kesslo. I have another company with the type of look we are chasing with your creative flair thrown in.

* We would like the Larkin the Plumber Logo to be as large as possible
on the side of the van along with the phone numbers

* The back of the van we would like the logo to be as large as possible with the phone numbers.

* We would like the Larkin the plumber web address www.larkintheplumber.com.au to be placed along bottom of vehicle as per the previous trucks. And of course phone numbers to be as large as possible without over bearing.

thanks
Marisol

```html
<!DOCTYPE html>
<html lang="en">
<head>
<meta charset="utf-8">
<title>Larkin the Plumber – Van Livery</title>
<link rel="stylesheet" href="https://fonts.googleapis.com/css2?family=Oswald:wght@500;600&display=swap">
<style>
  :root {
    --bg: #e4e5e7;
    --brand-blue: #1f4f9c;
    --brand-navy: #2a3590;
    --brand-red: #dd1b24;
    --van-white: #f7f7f7;
    --glass: #1b1d20;
    --trim: #3a3c40;
    --tyre: #202124;
    --hub: #b9bcc0;
    --light-lens: #c9ccd0;
    --tail: #b3141c;
    --logo-art: #dfe3ec;
    --text-light: #ffffff;
  }
  html, body { margin: 0; padding: 0; overflow: hidden; }
  body { width: 1200px; height: 1097px; background: var(--bg); }
  .livery { display: block; width: 1200px; height: 1097px; }
  .livery text { font-family: "Oswald", "Arial Narrow", sans-serif; font-weight: 500; }
  .fill-blue { fill: var(--brand-blue); }
  .fill-red { fill: var(--brand-red); }
  .fill-white { fill: var(--van-white); }
  .fill-glass { fill: var(--glass); }
  .fill-trim { fill: var(--trim); }
  .fill-tyre { fill: var(--tyre); }
  .fill-hub { fill: var(--hub); }
  .fill-lens { fill: var(--light-lens); }
  .fill-tail { fill: var(--tail); }
  .logo-badge { fill: #ffffff; stroke: var(--brand-red); stroke-width: 5; }
  .logo-art { fill: var(--logo-art); }
  .logo-name { fill: var(--brand-navy); font-weight: 600; letter-spacing: 1px; }
  .region-label { fill: var(--brand-red); }
  .phone-light { fill: var(--text-light); }
  .phone-navy { fill: var(--brand-navy); font-weight: 600; }
  .tagline-red { fill: var(--brand-red); }
  .tagline-light { fill: var(--text-light); }
  .web-text { fill: var(--text-light); font-weight: 600; }
  .phone-icon { fill: none; stroke: var(--text-light); stroke-width: 1.6; stroke-linecap: round; }
</style>
</head>
<body>
<svg class="livery" viewBox="0 0 1200 1097" xmlns="http://www.w3.org/2000/svg">
  <defs>
    <clipPath id="side-body">
      <path d="M72,372 L80,120 Q86,72 140,70 L620,70 Q682,72 724,112 L930,228 Q1000,240 1128,292 Q1148,302 1148,334 L1148,420 L1075,420 A82,82 0 0 0 911,420 L357,420 A82,82 0 0 0 193,420 L66,420 Z"/>
    </clipPath>
    <g id="phone-glyph">
      <path class="phone-icon" d="M3,2 Q1,4 3,8 Q6,13 10,14 Q12,14 13,12 L11,10 L9,11 Q6,9 5,6 L6,4 Z"/>
    </g>
  </defs>

  <!-- SIDE VIEW -->
  <g class="van-side">
    <g clip-path="url(#side-body)">
      <rect class="fill-white" x="60" y="60" width="1100" height="380"/>
      <path class="fill-red" d="M60,60 L470,60 Q520,300 660,360 Q760,400 910,422 L910,440 L60,440 Z"/>
      <path class="fill-blue" d="M60,60 L420,60 Q460,310 640,372 Q760,408 910,426 L910,440 L60,440 Z"/>
      <path class="fill-glass" d="M650,126 L836,126 Q850,128 870,150 L930,234 L650,242 Z"/>
      <rect class="fill-trim" x="1080" y="300" width="70" height="120"/>
    </g>
    <rect class="fill-trim" x="60" y="362" width="24" height="58" rx="6"/>
    <circle class="fill-tyre" cx="275" cy="420" r="74"/>
    <circle class="fill-hub" cx="275" cy="420" r="50"/>
    <circle class="fill-trim" cx="275" cy="420" r="14"/>
    <circle class="fill-tyre" cx="993" cy="420" r="74"/>
    <circle class="fill-hub" cx="993" cy="420" r="50"/>
    <circle class="fill-trim" cx="993" cy="420" r="14"/>

    <g class="logo-lockup">
      <circle class="logo-badge" cx="246" cy="219" r="150"/>
      <rect class="logo-art" x="186" y="138" width="120" height="92" rx="10" role="img" aria-label="Mascot illustration of a cheerful plumber in a cap holding a wrench and plunger"/>
      <text class="logo-name" x="246" y="270" font-size="24" text-anchor="middle">LARKIN THE PLUMBER</text>
    </g>

    <text class="region-label" x="393" y="303" font-size="15">Gold Coast</text>
    <use href="#phone-glyph" x="393" y="307"/>
    <text class="phone-light" x="414" y="323" font-size="20">(07) 5550 0142</text>
    <text class="region-label" x="393" y="350" font-size="15">Logan</text>
    <use href="#phone-glyph" x="393" y="354"/>
    <text class="phone-light" x="414" y="370" font-size="20">(07) 3555 0187</text>

    <rect class="fill-red" x="380" y="387" width="276" height="32" rx="16"/>
    <text class="web-text" x="518" y="410" font-size="19" text-anchor="middle">www.larkintheplumber.com.au</text>

    <text class="phone-navy" x="679" y="332" font-size="32">(07) 5550 0142</text>
    <text class="tagline-red" x="690" y="366" font-size="15">Dedicated Plumbing Specialists</text>
  </g>

  <!-- REAR VIEW -->
  <g class="van-rear">
    <rect class="fill-tyre" x="120" y="920" width="62" height="92" rx="12"/>
    <rect class="fill-tyre" x="485" y="920" width="62" height="92" rx="12"/>
    <path class="fill-blue" d="M150,590 Q160,566 200,564 L460,562 Q500,564 512,590 L542,760 L546,900 L118,900 L122,760 Z"/>
    <rect class="fill-tail" x="120" y="760" width="30" height="80" rx="4"/>
    <rect class="fill-tail" x="508" y="760" width="30" height="80" rx="4"/>
    <rect class="fill-lens" x="170" y="773" width="176" height="58" rx="8"/>
    <rect class="fill-trim" x="116" y="895" width="432" height="50" rx="10"/>

    <g class="logo-lockup">
      <circle class="logo-badge" cx="250" cy="745" r="97"/>
      <rect class="logo-art" x="212" y="690" width="76" height="60" rx="8" role="img" aria-label="Mascot illustration of a cheerful plumber in a cap holding a wrench and plunger"/>
      <text class="logo-name" x="250" y="779" font-size="15" text-anchor="middle">LARKIN THE PLUMBER</text>
    </g>

    <text class="tagline-light" x="364" y="655" font-size="17">DEDICATED</text>
    <text class="tagline-light" x="364" y="674" font-size="17">PLUMBING SPECIALISTS</text>
    <text class="region-label" x="364" y="698" font-size="11">Gold Coast</text>
    <use href="#phone-glyph" x="362" y="700"/>
    <text class="phone-light" x="381" y="714" font-size="16">(07) 5550 0142</text>
    <text class="region-label" x="364" y="735" font-size="11">Logan</text>
    <use href="#phone-glyph" x="362" y="737"/>
    <text class="phone-light" x="381" y="751" font-size="16">(07) 3555 0187</text>

    <rect class="fill-red" x="206" y="853" width="258" height="30" rx="15"/>
    <text class="web-text" x="335" y="875" font-size="17" text-anchor="middle">www.larkintheplumber.com.au</text>
  </g>

  <!-- FRONT VIEW -->
  <g class="van-front">
    <rect class="fill-tyre" x="662" y="930" width="60" height="82" rx="12"/>
    <rect class="fill-tyre" x="1058" y="930" width="60" height="82" rx="12"/>
    <path class="fill-white" d="M720,590 Q730,572 780,570 L1000,570 Q1048,572 1058,590 L1082,700 L1120,790 L1124,960 L658,960 L660,790 L698,700 Z"/>
    <path class="fill-glass" d="M722,612 L1058,612 L1064,722 L706,724 Z"/>
    <rect class="fill-white" x="654" y="678" width="36" height="52" rx="8"/>
    <rect class="fill-white" x="1094" y="684" width="44" height="46" rx="8"/>
    <path class="fill-trim" d="M672,790 Q700,778 756,800 L752,850 Q690,848 672,830 Z"/>
    <path class="fill-trim" d="M1108,790 Q1080,778 1024,800 L1028,850 Q1090,848 1108,830 Z"/>
    <rect class="fill-trim" x="758" y="812" width="264" height="34" rx="6"/>
    <rect class="fill-trim" x="678" y="910" width="424" height="34" rx="8"/>
    <circle class="fill-lens" cx="705" cy="925" r="12"/>
    <circle class="fill-lens" cx="1075" cy="925" r="12"/>

    <g class="logo-lockup">
      <circle class="logo-badge" cx="893" cy="772" r="48" style="stroke-width:3"/>
      <rect class="logo-art" x="875" y="745" width="36" height="28" rx="5" role="img" aria-label="Mascot illustration of a cheerful plumber"/>
      <text class="logo-name" x="893" y="791" font-size="7" text-anchor="middle" style="letter-spacing:0.5px">LARKIN THE PLUMBER</text>
    </g>
  </g>
</svg>
</body>
</html>
```